The Bright Socket Business cards

one side I would like my logo (uploaded) and the other side I want my details. I'm an electrician in sydney. The logo side I'm happy with just a white background and our logo in the middle.

Details for other side
24/7 Sydney Electrician
Marcus Hale
0431 758 216
marcus@thebrightsocket.com.au
thebrightsocket.com.au
icons for facebook, instagram, linked in

electrician

company info

```html
<!DOCTYPE html>
<html lang="en">
<head>
<meta charset="utf-8">
<title>The Bright Socket – Business Cards</title>
<link rel="stylesheet" href="https://fonts.googleapis.com/css2?family=Jost:wght@400;500;700&display=swap">
<style>
  :root {
    --bg: #e9e6e2;
    --card-white: #ffffff;
    --card-black: #0b0b0b;
    --red: #e3261f;
    --white: #ffffff;
    --grey-text: #e6e6e6;
  }
  html, body {
    margin: 0;
    padding: 0;
    width: 1200px;
    height: 900px;
    overflow: hidden;
    background: var(--bg);
    font-family: "Jost", "Futura", sans-serif;
  }
  .canvas {
    position: relative;
    width: 1200px;
    height: 900px;
  }
  .card {
    position: absolute;
    left: 320px;
    width: 560px;
    height: 320px;
    box-shadow: 0 10px 28px rgba(0,0,0,0.18);
    box-sizing: border-box;
  }
  .card-front {
    top: 70px;
    background: var(--card-white);
    border-radius: 26px;
    display: flex;
    align-items: center;
    justify-content: center;
  }
  .card-back {
    top: 470px;
    background: var(--card-black);
    border-radius: 6px 64px 6px 64px;
    color: var(--white);
  }
  .brand-name {
    font-family: "Jost", sans-serif;
    font-weight: 700;
    color: var(--red);
    text-transform: uppercase;
    letter-spacing: 0.04em;
    line-height: 1;
    margin: 0;
  }
  .card-front .brand-name { font-size: 42px; }
  .card-back .brand-name {
    position: absolute;
    right: 36px;
    top: 168px;
    font-size: 30px;
    line-height: 1.05;
    text-align: right;
  }
  .brand-line { display: block; }
  .details {
    position: absolute;
    left: 34px;
    top: 34px;
    width: 290px;
  }
  .person-name {
    margin: 0;
    color: var(--red);
    font-weight: 700;
    font-size: 19px;
    letter-spacing: 0.02em;
    text-transform: uppercase;
  }
  .person-role {
    margin: 0 0 12px;
    font-size: 15px;
    color: var(--grey-text);
  }
  .contact-list {
    list-style: none;
    margin: 0;
    padding: 0 0 0 8px;
  }
  .contact-item {
    display: flex;
    align-items: center;
    gap: 9px;
    font-size: 15px;
    color: var(--grey-text);
    margin-bottom: 5px;
    white-space: nowrap;
  }
  .contact-icon { width: 15px; height: 15px; flex: none; }
  .divider {
    width: 240px;
    height: 1.5px;
    background: var(--red);
    margin: 12px 0 10px 8px;
  }
  .tagline {
    margin: 0 0 0 8px;
    font-weight: 700;
    font-size: 19px;
    letter-spacing: 0.02em;
  }
  .social-row {
    position: absolute;
    left: 42px;
    bottom: 28px;
    display: flex;
    gap: 8px;
  }
  .social-dot {
    width: 26px;
    height: 26px;
    border-radius: 50%;
    background: var(--red);
  }
</style>
</head>
<body>
<main class="canvas">
  <section class="card card-front" aria-label="Business card front">
    <h1 class="brand-name">The Bright Socket</h1>
  </section>

  <section class="card card-back" aria-label="Business card back">
    <div class="details">
      <h2 class="person-name">Marcus Hale</h2>
      <p class="person-role">Director</p>
      <ul class="contact-list">
        <li class="contact-item">
          <svg class="contact-icon" viewBox="0 0 24 24" aria-hidden="true"><path fill="#e3261f" d="M6.6 10.8a15.1 15.1 0 0 0 6.6 6.6l2.2-2.2c.3-.3.7-.4 1-.2 1.1.4 2.3.6 3.6.6.6 0 1 .4 1 1V20c0 .6-.4 1-1 1A17 17 0 0 1 3 4c0-.6.4-1 1-1h3.5c.6 0 1 .4 1 1 0 1.3.2 2.5.6 3.6.1.3 0 .7-.2 1z"/></svg>
          0431 758 216
        </li>
        <li class="contact-item">
          <svg class="contact-icon" viewBox="0 0 24 24" aria-hidden="true"><path fill="#e3261f" d="M2 5h20v14H2z"/><path fill="none" stroke="#0b0b0b" stroke-width="2" d="M2 5l10 8 10-8"/></svg>
          marcus@thebrightsocket.com.au
        </li>
        <li class="contact-item">
          <svg class="contact-icon" viewBox="0 0 24 24" aria-hidden="true"><g fill="none" stroke="#e3261f" stroke-width="1.8"><circle cx="12" cy="12" r="9.5"/><ellipse cx="12" cy="12" rx="4" ry="9.5"/><path d="M2.5 12h19M4 7h16M4 17h16"/></g></svg>
          thebrightsocket.com.au
        </li>
      </ul>
      <div class="divider"></div>
      <p class="tagline">24/7 Sydney Electrician</p>
    </div>

    <p class="brand-name"><span class="brand-line">The Bright</span><span class="brand-line">Socket</span></p>

    <div class="social-row" aria-label="Social media links">
      <span class="social-dot"></span>
      <span class="social-dot"></span>
      <span class="social-dot"></span>
    </div>
  </section>
</main>
</body>
</html>
```